Cover Art Needed For Digital Single Release

We are looking to have the cover art designed for a new song called "Paper Lanterns". You will find the track attached below in a private TuneVault link so that you can have a listen.
We are thinking of keeping the artwork fairly simple but still want it to catch your eye. Maybe using the song title and artist’s name in a colorful and creative way. (A well-designed font with a bold color scheme, or even something like a mosaic style art piece featuring the title).
We completely welcome any and all creative visions you might have, even if it strays away from the examples given above.
Thank you in advance for your submissions, and we are excited to collaborate with you!
"Paper Lanterns" by Marcus Holloway
https://tunevault.example/marcusxyz/paper-lanterns/s-r7Tq2wLmNcx
Target Market(s)
Teens/Young Adults
Industry/Entity Type
Music
Requirements
Must have
- An eye-catching design
Should not have
- Please do not rely heavily on stock images. We prefer an original design/concept.

```html
<!DOCTYPE html>
<html lang="en">
<head>
<meta charset="utf-8">
<title>Paper Lanterns — Marcus Holloway</title>
<link rel="stylesheet" href="https://fonts.googleapis.com/css2?family=Abril+Fatface&family=DM+Serif+Display:ital@0;1&display=swap">
<style>
  :root {
    --grey: #8b8b8b;
    --grey-warm: #9a938a;
    --steel-yellow: #d9b73a;
    --plum: #3b2450;
    --orange: #ff8a00;
    --amber: #d39a00;
    --yellow: #ffe600;
    --olive: #9a8a10;
    --lavender: #b56cf2;
    --indigo: #3c1fd0;
    --ink: #26232c;
    --white: #ffffff;
  }
  * { margin: 0; padding: 0; box-sizing: border-box; }
  html, body { width: 1200px; height: 1176px; overflow: hidden; background: var(--grey); }
  .cover {
    position: relative;
    width: 1200px;
    height: 1176px;
    overflow: hidden;
  }
  .backdrop {
    position: absolute; inset: 0;
    background:
      linear-gradient(180deg, transparent 0 82%, rgba(217,183,58,.85) 84%, rgba(200,170,60,.75) 94%, transparent 96%),
      linear-gradient(90deg, var(--grey-warm) 0 30%, var(--grey) 30% 100%),
      var(--grey);
  }
  .backdrop::after {
    content: "";
    position: absolute; inset: 0;
    background:
      linear-gradient(125deg, transparent 0 18%, rgba(217,183,58,.45) 18.5% 20%, transparent 20.5%),
      linear-gradient(60deg, transparent 0 48%, rgba(217,183,58,.35) 48.5% 50%, transparent 50.5%),
      linear-gradient(0deg, transparent 0 96%, rgba(217,183,58,.6) 96.5% 99%, transparent 99.5%);
  }

  .title, .artist { position: absolute; left: 0; width: 1200px; }
  .layer {
    position: absolute; left: 0; top: 0; width: 100%;
    white-space: nowrap; line-height: 1;
  }

  .title-line { position: absolute; left: 0; width: 1200px; height: 320px; }
  .title-line .layer { font-family: "Abril Fatface", "DM Serif Display", serif; text-align: center; }
  .line-one { top: 40px; }
  .line-two { top: 330px; }
  .line-one .layer { font-size: 250px; letter-spacing: -4px; }
  .line-two .layer { font-size: 225px; letter-spacing: -6px; }

  .tone-plum     { color: var(--plum); opacity: .85; }
  .tone-orange   { color: var(--orange); opacity: .7; mix-blend-mode: multiply; }
  .tone-yellow   { color: transparent; -webkit-text-stroke: 10px var(--yellow); opacity: .85; }
  .tone-olive    { color: var(--olive); opacity: .6; }
  .tone-lavender { color: var(--lavender); opacity: .8; }
  .tone-indigo   { color: var(--indigo); opacity: .55; mix-blend-mode: multiply; }
  .tone-ink      { color: var(--ink); opacity: .8; }
  .tone-white    { color: var(--white); opacity: .9; font-size: .55em !important; }

  .artist { top: 830px; height: 180px; }
  .artist .layer {
    font-family: "DM Serif Display", serif;
    font-size: 128px;
    letter-spacing: -3px;
    text-align: center;
  }
  .artist .name-white  { color: var(--white); }
  .artist .name-yellow { color: var(--yellow); opacity: .9; }
  .artist .name-amber  { color: var(--amber); opacity: .8; }
  .artist .name-shadow { color: var(--grey); opacity: .5; font-style: italic; }

  .waveform {
    position: absolute;
    left: 505px; top: 1030px;
    width: 625px; height: 80px;
    background: repeating-linear-gradient(90deg, rgba(240,230,250,.9) 0 2px, transparent 2px 5px);
    clip-path: polygon(0 60%, 2% 20%, 10% 12%, 20% 18%, 28% 8%, 38% 15%, 46% 5%, 55% 14%, 62% 10%, 72% 16%, 82% 12%, 92% 20%, 98% 45%, 100% 60%, 98% 75%, 92% 88%, 82% 92%, 72% 90%, 62% 95%, 55% 90%, 46% 96%, 38% 90%, 28% 94%, 20% 88%, 10% 90%, 2% 82%);
  }
</style>
</head>
<body>
<main class="cover">
  <div class="backdrop" role="img" aria-label="Low-angle photograph of yellow steel scaffolding with grated walkways against a grey sky"></div>

  <h1 class="title" aria-label="Paper Lanterns">
    <div class="title-line line-one" aria-hidden="true">
      <span class="layer tone-olive" style="transform:translate(40px,-10px)">paper</span>
      <span class="layer tone-orange" style="transform:translate(-30px,20px)">paper</span>
      <span class="layer tone-plum" style="transform:translate(10px,0)">paper</span>
      <span class="layer tone-yellow" style="transform:translate(-55px,30px)">paper</span>
      <span class="layer tone-lavender" style="transform:translate(20px,60px) scale(.9)">paper</span>
      <span class="layer tone-white" style="transform:translate(20px,120px)">paper</span>
    </div>
    <div class="title-line line-two" aria-hidden="true">
      <span class="layer tone-lavender" style="transform:translate(-20px,20px)">lanterns</span>
      <span class="layer tone-orange" style="transform:translate(25px,-10px)">lanterns</span>
      <span class="layer tone-indigo" style="transform:translate(10px,30px)">lanterns</span>
      <span class="layer tone-ink" style="transform:translate(0,5px)">lanterns</span>
      <span class="layer tone-yellow" style="transform:translate(-40px,40px)">lanterns</span>
      <span class="layer tone-olive" style="transform:translate(30px,20px) scale(.92)">lanterns</span>
      <span class="layer tone-white" style="transform:translate(0,95px)">lanterns</span>
    </div>
  </h1>

  <h2 class="artist" aria-label="Marcus Holloway">
    <span class="layer name-shadow" aria-hidden="true" style="transform:translate(6px,30px)">Marcus Holloway</span>
    <span class="layer name-amber" aria-hidden="true" style="transform:translate(-14px,10px)">Marcus Holloway</span>
    <span class="layer name-yellow" aria-hidden="true" style="transform:translate(-6px,4px)">Marcus Holloway</span>
    <span class="layer name-white">Marcus Holloway</span>
  </h2>

  <div class="waveform" aria-hidden="true"></div>
</main>
</body>
</html>
```